Quillet Studios business card

Front of card should be logo and back of card should be communication info.
Please note: reverse the logo color. Card should be black and everything else white.

Industry/Entity Type

Custom home design/construction

Contact Information for Business Card

Quillet Studios, LLC 555-382-0146 quilletstudios@mailbox-example.com

Requirements
Must have
• Square card, Logo on front, communication info on back and perhaps a mini version of the logo on back also. Black card/white lettering. Double sides square card.
Nice to have
• I want to keep it simple. Our product (custom homes) speak for themselves.

```html
<!DOCTYPE html>
<html lang="en">
<head>
<meta charset="utf-8">
<title>Quillet Studios – Square Business Card</title>
<link rel="stylesheet" href="https://fonts.googleapis.com/css2?family=Outfit:wght@300;400;500;600;700&display=swap">
<style>
  :root {
    --page-bg: #ecebe8;
    --card-black: #000000;
    --ink-white: #ffffff;
    --art-tone: #1c1c1c;
    --card-size: 555px;
    --card-radius: 56px;
  }
  * { box-sizing: border-box; margin: 0; padding: 0; }
  html, body {
    width: 1200px;
    height: 1200px;
    overflow: hidden;
    background: var(--page-bg);
    font-family: "Outfit", sans-serif;
  }
  .sheet {
    position: relative;
    width: 1200px;
    height: 1200px;
  }
  .card {
    position: absolute;
    left: 322px;
    width: var(--card-size);
    height: var(--card-size);
    background: var(--card-black);
    border-radius: var(--card-radius);
    overflow: hidden;
    color: var(--ink-white);
    box-shadow: 0 4px 14px rgba(0,0,0,0.18);
  }
  .card--front { top: 34px; }
  .card--back  { top: 611px; }

  .brand-name {
    position: absolute;
    left: 0;
    right: 0;
    text-align: center;
    font-weight: 600;
    font-size: 44px;
    letter-spacing: 0.6px;
    white-space: nowrap;
    line-height: 1;
  }
  .brand-tagline {
    position: absolute;
    left: 0;
    right: 0;
    text-align: center;
    font-weight: 300;
    font-size: 20px;
    letter-spacing: 7.6px;
    white-space: nowrap;
    line-height: 1;
  }
  .card--front .brand-name { top: 379px; padding-left: 16px; }
  .card--front .brand-tagline { top: 429px; padding-left: 34px; }
  .card--back .brand-name { top: 168px; }
  .card--back .brand-tagline { top: 217px; padding-left: 10px; }

  .house-art {
    position: absolute;
    background: var(--art-tone);
  }
  .house-art--front { left: 106px; top: 119px; width: 348px; height: 244px; }
  .house-art--back  { left: 288px; top: 279px; width: 267px; height: 276px; }

  .back-details {
    position: absolute;
    left: 45px;
    top: 330px;
    width: 235px;
  }
  .person-name {
    font-size: 28px;
    font-weight: 400;
    line-height: 1;
    padding-left: 1px;
  }
  .person-role {
    margin-top: 8px;
    font-size: 18px;
    font-weight: 400;
    line-height: 1;
  }
  .contact-list {
    margin-top: 46px;
    list-style: none;
  }
  .contact-item {
    display: flex;
    align-items: center;
    height: 22.5px;
    font-size: 16.5px;
    font-weight: 500;
    letter-spacing: 0.3px;
    white-space: nowrap;
  }
  .contact-icon {
    width: 18px;
    height: 18px;
    margin-right: 11px;
    flex: none;
  }
</style>
</head>
<body>
<main class="sheet">

  <section class="card card--front" aria-label="Card front">
    <div class="house-art house-art--front" role="img" aria-label="Line drawing of a two-storey custom home with dormers and porch"></div>
    <h1 class="brand-name">QUILLET STUDIOS</h1>
    <p class="brand-tagline">CUSTOM HOME BUILDERS</p>
  </section>

  <section class="card card--back" aria-label="Card back">
    <h2 class="brand-name">QUILLET STUDIOS</h2>
    <p class="brand-tagline">CUSTOM HOME BUILDERS</p>

    <div class="house-art house-art--back" role="img" aria-label="Cropped line drawing of the custom home, bottom right corner"></div>

    <div class="back-details">
      <p class="person-name">Mara Ellison</p>
      <p class="person-role">Director</p>

      <ul class="contact-list">
        <li class="contact-item">
          <svg class="contact-icon" viewBox="0 0 24 24" aria-hidden="true"><path fill="#fff" d="M6.6 2.5l3 3.6c.4.5.4 1.2 0 1.7L7.9 9.6c1.3 2.8 3.6 5.1 6.5 6.5l1.8-1.7c.5-.4 1.2-.4 1.7 0l3.6 3c.5.4.6 1.1.2 1.7l-1.6 2.2c-.5.6-1.300.9-2 .7C10 20.3 3.7 14 2 6.1c-.2-.8.1-1.6.7-2l2.2-1.6c.6-.4 1.3-.4 1.7 0z"/></svg>
          555-382-0146
        </li>
        <li class="contact-item">
          <svg class="contact-icon" viewBox="0 0 24 24" aria-hidden="true"><rect x="2" y="5" width="20" height="14" fill="none" stroke="#fff" stroke-width="2"/><path d="M2 5l10 8 10-8M2 19l7.5-7M22 19l-7.5-7" fill="none" stroke="#fff" stroke-width="2"/></svg>
          mara@quillet.example
        </li>
        <li class="contact-item">
          <svg class="contact-icon" viewBox="0 0 24 24" aria-hidden="true"><g fill="none" stroke="#fff" stroke-width="2"><circle cx="12" cy="12" r="9.5"/><ellipse cx="12" cy="12" rx="4" ry="9.5"/><path d="M2.5 12h19M4 7h16M4 17h16"/></g></svg>
          quillet.example
        </li>
      </ul>
    </div>
  </section>

</main>
</body>
</html>
```